Inflatable Movie Screen company needs a Brochure Design for sales kit

We need a brochure as per attached sketch drawing which is to:
1)follow the sample layout
2) attached images must be used
3) to follow company corporate colors or suggest something professional and appropriate for the theme
Updates

Target Market(s)

Corporate and Community Clubs

Industry/Entity Type

Entertainment

Requirements
Must have
• Colors to be in line with corporate colors OR to suggest something appropriate.
Nice to have
• A unique concept
Should not have
• Too fanciful

```html
<!DOCTYPE html>
<html lang="en">
<head>
<meta charset="utf-8">
<title>Inflatable Movie Screening Brochure</title>
<link rel="stylesheet" href="https://fonts.googleapis.com/css2?family=Great+Vibes&family=Lato:wght@400;700;900&display=swap">
<style>
  :root {
    --paper: #ffffff;
    --stage: #e9ebe4;
    --ink: #1b1b1b;
    --charcoal: #2b2c2e;
    --grey: #8d8d8f;
    --grey-light: #c9c9cb;
    --grey-pale: #ececee;
    --lawn: #4f7a3a;
    --night: #34486a;
  }
  * { margin: 0; padding: 0; box-sizing: border-box; }
  html, body { width: 1200px; height: 848px; overflow: hidden; background: var(--stage); }
  .spread { display: flex; width: 1200px; height: 848px; }
  .page { position: relative; width: 600px; height: 848px; background: var(--paper); overflow: hidden; }
  .page svg { position: absolute; inset: 0; }
  .back-cover { border-right: 1px solid var(--grey-light); }

  .brand-plate {
    position: absolute; left: 205px; top: 478px; width: 190px; height: 72px;
    background: var(--grey); display: flex; flex-direction: column;
    align-items: center; justify-content: center; color: var(--paper);
    font-family: "Lato", sans-serif; font-weight: 400;
  }
  .brand-name { font-size: 26px; letter-spacing: 1px; }
  .brand-sub { font-size: 7px; letter-spacing: 1.5px; margin-top: 2px; }

  .contact { position: absolute; left: 0; right: 0; top: 585px; text-align: center; font-family: "Lato", sans-serif; color: var(--ink); }
  .contact-title { font-size: 28px; font-weight: 900; letter-spacing: 0.5px; }
  .contact-box {
    margin: 14px auto 0; width: 330px; padding: 12px 16px;
    border: 2px solid var(--ink); border-radius: 18px;
  }
  .contact-line { font-size: 15px; font-weight: 400; line-height: 1.5; }
  .contact-phone { font-size: 24px; font-weight: 700; line-height: 1.3; }
  .web { font-family: "Lato", sans-serif; font-weight: 700; font-size: 16px; letter-spacing: 7px; color: var(--ink); }
  .back-cover .web { position: absolute; left: 0; right: 0; top: 790px; text-align: center; }

  .title {
    position: absolute; left: 120px; top: 22px; width: 460px; text-align: center;
    font-family: "Great Vibes", cursive; font-size: 54px; line-height: 1.05; color: var(--ink);
  }
  .badge {
    position: absolute; left: 365px; top: 165px; width: 190px; height: 190px; border-radius: 50%;
    background: var(--grey); border: 6px solid var(--paper); box-shadow: 0 0 0 2px var(--grey);
    display: flex; flex-direction: column; align-items: center; justify-content: center;
    color: var(--paper); font-family: "Lato", sans-serif; font-weight: 400;
  }
  .badge .brand-name { font-size: 27px; }
  .quote {
    position: absolute; left: 120px; top: 592px; width: 450px;
    font-family: "Lato", sans-serif; color: var(--paper);
  }
  .quote-text { font-size: 11px; line-height: 1.45; }
  .quote-mark { font-weight: 900; font-size: 16px; }
  .quote-source { text-align: right; font-size: 15px; font-weight: 700; margin-top: 4px; }
  .front-cover .web { position: absolute; left: 120px; width: 450px; top: 722px; text-align: center; }
</style>
</head>
<body>
<main class="spread">

  <section class="page back-cover">
    <svg width="600" height="848" viewBox="0 0 600 848">
      <defs>
        <linearGradient id="band-back" x1="0" y1="0" x2="1" y2="0">
          <stop offset="0" stop-color="#b9b9bb"/>
          <stop offset="1" stop-color="#7b7b7d"/>
        </linearGradient>
        <linearGradient id="park-photo" x1="0" y1="0" x2="0" y2="1">
          <stop offset="0" stop-color="#5b7f58"/>
          <stop offset="0.35" stop-color="var(--night)"/>
          <stop offset="0.6" stop-color="#6d8a5c"/>
          <stop offset="1" stop-color="#ffffff"/>
        </linearGradient>
        <linearGradient id="park-fade" x1="0" y1="0" x2="1" y2="0">
          <stop offset="0.45" stop-color="#ffffff" stop-opacity="0"/>
          <stop offset="1" stop-color="#ffffff" stop-opacity="0.85"/>
        </linearGradient>
      </defs>
      <rect width="600" height="848" fill="var(--paper)"/>
      <g role="img" aria-label="Evening crowd seated on a park lawn watching an outdoor screen under lit trees">
        <path d="M0 0 H600 V500 H0 Z" fill="url(#park-photo)"/>
        <path d="M0 0 H600 V500 H0 Z" fill="url(#park-fade)"/>
      </g>
      <path d="M0 0 H600 V40 C470 30 380 200 170 210 C90 214 40 200 0 195 Z" fill="url(#band-back)"/>
      <path d="M0 195 C40 200 90 214 170 210 C380 200 470 30 600 40" fill="none" stroke="var(--ink)" stroke-width="3"/>
      <path d="M0 215 C60 222 110 232 190 226 C390 214 480 60 600 55" fill="none" stroke="var(--paper)" stroke-width="6"/>
    </svg>
    <div class="brand-plate">
      <span class="brand-name">LUMENFIELD</span>
      <span class="brand-sub">LUMENFIELD EVENTS PTY LTD</span>
    </div>
    <div class="contact">
      <h2 class="contact-title">CONTACT US:</h2>
      <div class="contact-box">
        <p class="contact-line">EMAIL: LOREM @lorem ipsum</p>
        <p class="contact-phone">CALL US: 123 456 7890</p>
        <p class="contact-line">EMAIL: LOREM @lorem ipsum</p>
      </div>
    </div>
    <p class="web">www.lorem.com</p>
  </section>

  <section class="page front-cover">
    <svg width="600" height="848" viewBox="0 0 600 848">
      <defs>
        <linearGradient id="band-front" x1="0" y1="0" x2="1" y2="0">
          <stop offset="0" stop-color="#9c9c9e"/>
          <stop offset="0.5" stop-color="#e4e4e6"/>
          <stop offset="1" stop-color="#ffffff"/>
        </linearGradient>
        <linearGradient id="lawn-photo" x1="0" y1="0" x2="0" y2="1">
          <stop offset="0" stop-color="#cfd6e0"/>
          <stop offset="0.45" stop-color="#6f8fa8"/>
          <stop offset="1" stop-color="var(--lawn)"/>
        </linearGradient>
        <linearGradient id="grey-photo" x1="0" y1="0" x2="1" y2="0">
          <stop offset="0" stop-color="#a9a9ab"/>
          <stop offset="1" stop-color="#dcdcde"/>
        </linearGradient>
      </defs>
      <rect width="600" height="848" fill="var(--paper)"/>
      <path d="M0 160 C120 170 230 250 360 262 L360 300 C230 290 100 230 0 230 Z" fill="url(#band-front)"/>
      <g role="img" aria-label="Crowd seated on a lawn facing an inflatable movie screen beside a lit building">
        <path d="M0 230 C100 230 230 290 360 300 L380 340 C420 420 470 460 520 500 L520 590 H60 V620 H0 Z" fill="url(#lawn-photo)"/>
      </g>
      <g role="img" aria-label="Faded black and white view of an audience">
        <path d="M560 230 C590 300 560 430 500 500 L520 590 H600 V220 Z" fill="url(#grey-photo)"/>
      </g>
      <path d="M0 160 C120 170 230 250 360 262" fill="none" stroke="var(--ink)" stroke-width="3"/>
      <path d="M470 360 C500 430 520 520 510 660" fill="none" stroke="var(--grey-light)" stroke-width="5"/>
      <rect x="60" y="580" width="540" height="92" fill="var(--charcoal)"/>
      <path d="M560 570 C600 600 600 650 580 690" fill="none" stroke="var(--grey-light)" stroke-width="5"/>
    </svg>
    <h1 class="title">Inflatable Movie<br>Screening by</h1>
    <div class="badge">
      <span class="brand-name">LUMENFIELD</span>
      <span class="brand-sub">LUMENFIELD EVENTS PTY LTD</span>
    </div>
    <blockquote class="quote">
      <p class="quote-text"><span class="quote-mark">&ldquo;</span> Lorem Ipsum is simply dummy text of the printing and typesetting industry. Lorem Ipsum has been the industry's standard dummy text ever since the 1500s, when an unknown printer took a galley of type and scrambled it to make a type specimen book. <span class="quote-mark">&rdquo;</span></p>
      <p class="quote-source">- Lorem Ipsum Text</p>
    </blockquote>
    <p class="web">www.lorem.com</p>
  </section>

</main>
</body>
</html>
```